Velmarin is a skin care brand, currently selling in India. We want to make design for our new la...

We want to develop label design for our new launch sunscreen . It is Anti-pollution sunscreen with SPF 50

Colors

Designer to choose colors to be used in the design.

```html
<!DOCTYPE html>
<html lang="en">
<head>
<meta charset="utf-8">
<title>Velmarin Anti-Pollution Sunscreen SPF 50 – Label</title>
<link rel="stylesheet" href="https://fonts.googleapis.com/css2?family=Jost:wght@300;400;600&family=Oswald:wght@700&family=Source+Sans+3:wght@400;600&display=swap">
<style>
  :root {
    --backdrop: #f0efea;
    --label-top: #d8d22a;
    --label-mid: #ddb24a;
    --label-bottom: #c7782c;
    --navy: #1e2a78;
    --navy-glow: #3a48c8;
    --ink: #2b2418;
    --spf-yellow: #e6c224;
    --pale: #fbeecb;
    --white: #ffffff;
  }
  * { margin: 0; padding: 0; box-sizing: border-box; }
  html, body {
    width: 1200px; height: 1115px; overflow: hidden;
    background: var(--backdrop);
  }
  .canvas { position: relative; width: 1200px; height: 1115px; }
  .label {
    position: absolute; left: 380px; top: 100px;
    width: 440px; height: 916px;
    border-radius: 6px;
    background: linear-gradient(180deg, var(--label-top) 0%, #dcc63a 30%, var(--label-mid) 62%, var(--label-bottom) 100%);
    font-family: "Jost", sans-serif;
    color: var(--ink);
    text-align: center;
  }
  .label > * { position: absolute; left: 50%; transform: translateX(-50%); white-space: nowrap; }
  .brand-dot {
    top: 68px; width: 112px; height: 112px; border-radius: 50%;
    background: var(--navy);
  }
  .brand-name {
    top: 150px; width: 260px; height: 52px;
    background: var(--navy);
    color: var(--white);
    font-weight: 400; font-size: 34px; letter-spacing: 2px; line-height: 52px;
  }
  .product-line {
    top: 226px; font-weight: 300; font-size: 44px; letter-spacing: -1px; line-height: 1;
  }
  .product-type {
    top: 278px; font-weight: 300; font-size: 58px; letter-spacing: -1px; line-height: 1;
  }
  .spf-badge {
    top: 348px; width: 210px; height: 60px;
    background: radial-gradient(ellipse at 30% 60%, var(--navy-glow), var(--navy) 70%);
    color: var(--spf-yellow);
    font-family: "Oswald", sans-serif; font-weight: 700; font-size: 56px; line-height: 58px;
  }
  .spf-note { top: 418px; font-size: 14.5px; font-weight: 400; letter-spacing: -0.3px; }
  .ingredient-badge {
    top: 440px; width: 197px; height: 197px; border-radius: 50%;
    background: radial-gradient(circle at 45% 40%, #ffffff 0%, #eef0ea 55%, #d6dccf 100%);
  }
  .ingredient-title {
    top: 465px; font-size: 17px; font-weight: 400; letter-spacing: 3px;
  }
  .ingredient-art {
    top: 498px; width: 130px; height: 120px; border-radius: 50% 50% 40% 40%;
    background: radial-gradient(ellipse at 50% 70%, #6f9a3c, #9bc06a 60%, rgba(155,192,106,0) 75%);
  }
  .claim-title {
    top: 648px; font-family: "Source Sans 3", sans-serif; font-weight: 600; font-size: 19px; letter-spacing: -0.3px;
  }
  .claim-list {
    top: 676px; list-style: none;
    font-family: "Source Sans 3", sans-serif; font-size: 15.5px; line-height: 18.5px; color: var(--pale);
  }
  .divider { top: 752px; width: 184px; height: 2px; background: var(--ink); }
  .benefit-list {
    top: 778px; list-style: none;
    font-family: "Source Sans 3", sans-serif; font-size: 11.5px; line-height: 18px; letter-spacing: -0.2px; color: #3a2a14;
  }
  .net-volume { top: 880px; font-weight: 600; font-size: 21px; letter-spacing: 1.5px; }
</style>
</head>
<body>
<div class="canvas">
  <section class="label">
    <div class="brand-dot"></div>
    <div class="brand-name">VELMARIN</div>
    <h1 class="product-line">ANTI-POLLUTION</h1>
    <h2 class="product-type">SUNSCREEN</h2>
    <div class="spf-badge">SPF 50</div>
    <p class="spf-note">SUN + POLLUTION PROTECTION</p>
    <div class="ingredient-badge"></div>
    <p class="ingredient-title">ALOE VERA</p>
    <div class="ingredient-art" role="img" aria-label="Aloe vera plant illustration"></div>
    <p class="claim-title">WATER RESISTANT SUNSCREEN</p>
    <ul class="claim-list">
      <li>GOOD SPREAD ABILITY</li>
      <li>NON GREASY &amp; NON OILY</li>
      <li>NON IRRITATING</li>
      <li>NO PARABENS &amp; NO MINERAL OIL</li>
    </ul>
    <div class="divider"></div>
    <ul class="benefit-list">
      <li>CONTAINS ALOE VERA TO PROVIDE SOOTHING EFFECT ON SKIN</li>
      <li>PROTECT AGAINST POLLUTANT PARTICLES UP TO 2.5 MICRONS</li>
      <li>PROVIDES PROTECTION FROM UVA &amp; UVB RAYS</li>
      <li>SUITABLE FOR ALL SKIN TYPES</li>
    </ul>
    <p class="net-volume">80 ml</p>
  </section>
</div>
</body>
</html>
```